Need 5 pages of a marketing website designed

Need a simple site about a "mountain-town" digital marketing company designed around these topics. (UNCODED)
The homepage can mention these topics
- Website Creation / Management (New or Existing Websites & Hosting)
- Findora Search Marketing (Get Found in Findora Organic!)
- Social Media Marketing (Paid & Free Versions)
- Findora Shopfront Management (Get Found in Findora Atlas!)
- Video Content Creation & Marketing (Great for Vidspring & SM)
- Blog Content Creation & Marketing (Great for Findora & SM)
- Digital Marketing Consulting (Understand Best Marketing Options Based on Niche)
- Small Business Services (Phone Tracking Software / ROI Consulting / SOP Development)
And 1 service page created around 1 of the topics mentioned above (Ex - Social Media Marketing services), which I can duplicate for the other service pages
Please create these pages also
> Contact Us
> About Us
> Testimonials
Must be themed around Mountain Towns / ski resorts
I'm open to white / black / minor blues or orange for important areas
Can use Ipsum content for the text, just please create the headings etc
Lmk if you have any questions please

```html
<!DOCTYPE html>
<html lang="en">
<head>
<meta charset="utf-8">
<title>Our Services – Summit Ridge Marketing</title>
<link href="https://fonts.googleapis.com/css2?family=Inter:wght@400;500;600;700;800&display=swap" rel="stylesheet">
<style>
:root{
  --navy:#0b2f4e;
  --navy-deep:#082640;
  --blue:#1479bd;
  --blue-bright:#1a84c6;
  --ink:#1b2430;
  --text:#4d5763;
  --muted:#7a838d;
  --panel:#eef6fd;
  --line:#dfe5eb;
  --white:#ffffff;
}
*{margin:0;padding:0;box-sizing:border-box}
html,body{width:1200px;height:3829px;overflow:hidden}
body{font-family:'Inter',sans-serif;color:var(--text);background:var(--white);position:relative}
.abs{position:absolute}
.topline{left:0;top:0;width:1200px;height:3px;background:var(--blue)}

/* header */
.brand{left:145px;top:36px;width:220px;font-weight:800;font-size:26px;line-height:30px;color:var(--navy);letter-spacing:.5px;text-transform:uppercase}
.contact-chip{top:22px;display:flex;align-items:center;gap:12px}
.contact-chip .ic{width:36px;height:36px;border-radius:50%;background:var(--blue);display:flex;align-items:center;justify-content:center}
.contact-chip small{display:block;font-size:11px;color:var(--muted)}
.contact-chip b{display:block;font-size:14px;color:var(--navy);font-weight:700;margin-top:3px}
.chip-mail{left:600px}
.chip-mail b{font-size:13px}
.chip-phone{left:866px}
.chip-phone b{font-size:17px}
.navbar{left:440px;top:83px;width:760px;height:41px;background:var(--navy);clip-path:polygon(28px 0,100% 0,100% 100%,0 100%)}
.nav{left:463px;top:83px;display:flex;height:41px}
.nav a{display:flex;align-items:center;padding:0 15px;color:var(--white);font-size:14px;font-weight:500;text-decoration:none}
.nav a.active{background:var(--blue-bright)}

/* hero */
.hero{left:0;top:124px;width:1200px;height:376px;background:linear-gradient(180deg,#5d7ea6 0%,#a9bfd6 28%,#e9eef4 58%,#f9fafc 100%)}
.hero-title{left:145px;top:270px;font-size:47px;font-weight:800;color:var(--navy);letter-spacing:.5px}

/* intro */
.intro-h{left:145px;top:552px;width:370px;font-size:31px;line-height:37px;font-weight:700;color:var(--navy)}
.intro-h span{color:var(--blue)}
.intro-q{left:145px;top:642px;width:360px;font-size:15.5px;line-height:26px;font-weight:600;color:#3b4652}
.para{font-size:12.8px;line-height:21.5px;color:var(--text);text-align:justify}
.intro-p{left:575px;top:552px;width:481px}
.intro-p p+p{margin-top:14px}
.photo{border-radius:1px}
.ph1{left:145px;top:730px;width:355px;height:270px;background:linear-gradient(135deg,#3b2a26,#8a5e45 55%,#d6a57a)}
.ph2{left:514px;top:851px;width:271px;height:149px;background:linear-gradient(135deg,#2a2430,#6b4a3a 60%,#b58b62)}
.ph3{left:273px;top:1014px;width:227px;height:182px;background:linear-gradient(135deg,#123a5c,#3a7fa8 55%,#c7a57a)}
.ph4{left:514px;top:1014px;width:542px;height:239px;background:linear-gradient(135deg,#c9c2b6,#e2c35a 30%,#8b6a52 65%,#3f3a3c)}
.body-p{left:145px;top:1304px;width:911px}
.body-p p+p{margin-top:14px}

/* mountain bands */
.band{left:0;width:1200px;height:170px;background:linear-gradient(180deg,rgba(255,255,255,0) 0%,#b7c9dc 35%,#dfe8f1 65%,#ffffff 100%)}
.band1{top:1495px}
.band2{top:2072px}

/* approach */
.eyebrow{font-size:12px;font-weight:700;color:var(--blue);text-transform:uppercase;letter-spacing:.3px}
.app-eyebrow{left:0;width:1200px;top:1703px;text-align:center}
.app-h{left:0;width:1200px;top:1728px;text-align:center;font-size:35px;font-weight:700;color:var(--navy)}
.step{top:1810px;width:290px;text-align:center}
.step .badge{width:90px;height:90px;margin:0 auto;border-radius:50%;background:var(--navy);border:3px solid #1c4d75;display:flex;align-items:center;justify-content:center}
.step h3{margin-top:24px;font-size:17px;font-weight:700;color:var(--navy)}
.step p{margin-top:10px;font-size:12.8px;line-height:21.5px;color:var(--text)}
.s1{left:140px}.s2{left:454px}.s3{left:768px}

/* cta heading */
.ready{left:0;width:1200px;top:2306px;text-align:center;font-size:32px;line-height:42px;font-weight:700;color:var(--navy)}

/* contact */
.c-eyebrow{left:145px;top:2450px;font-size:12px;font-weight:500;color:var(--blue)}
.c-h{left:145px;top:2478px;font-size:32px;font-weight:600;color:var(--navy)}
.c-sub{left:145px;top:2530px;font-size:18px;color:var(--text)}
.info-card{left:145px;width:386px;height:88px;background:var(--white);border:1px solid var(--line);border-radius:3px;box-shadow:0 2px 8px rgba(11,47,78,.06);display:flex;align-items:center;padding-left:24px;gap:14px}
.info-card b{display:block;font-size:14px;font-weight:600;color:var(--navy)}
.info-card span{display:block;font-size:12.5px;color:var(--text);margin-top:6px}
.card1{top:2585px}.card2{top:2695px}.card3{top:2804px}
.enquire{left:573px;top:2450px;width:510px;height:443px;background:var(--panel)}
.enquire h2{position:absolute;left:27px;top:26px;font-size:21px;font-weight:600;color:var(--navy)}
.field{position:absolute;left:27px;width:456px;height:36px;background:var(--white);border:1px solid var(--line);display:flex;align-items:center;justify-content:space-between;padding:0 14px;font-size:12px;color:#5d6670}
.field i{color:#d62020;font-style:normal}
.f1{top:76px}.f2{top:127px}.f3{top:177px}.f4{top:228px}
.f5{top:278px;height:74px;align-items:flex-start;padding-top:10px}
.submit{position:absolute;left:27px;top:377px;width:456px;height:38px;background:linear-gradient(90deg,#1479bd,#0b2f4e);color:var(--white);font-size:12px;font-weight:700;display:flex;align-items:center;justify-content:center;gap:8px}

/* forest + consultation */
.forest{left:0;top:2930px;width:1200px;height:337px;background:linear-gradient(180deg,#ffffff 0%,#c7d5e2 30%,#8fa6ba 65%,#4f6a80 100%)}
.consult{left:0;top:3267px;width:1200px;height:258px;background:var(--blue-bright)}
.person{left:178px;top:3180px;width:264px;height:345px;background:linear-gradient(180deg,#4a3227 0%,#e9e6e2 40%,#3d5d8a 100%);border-radius:120px 120px 0 0}
.consult-eyebrow{left:540px;width:380px;top:3337px;text-align:center;font-size:12px;font-weight:700;color:var(--white)}
.consult-h{left:440px;width:580px;top:3358px;text-align:center;font-size:35px;font-weight:700;color:var(--white)}
.consult-btn{left:642px;top:3405px;width:177px;height:40px;background:var(--navy-deep);color:var(--white);font-size:12px;font-weight:700;display:flex;align-items:center;justify-content:center;gap:8px}

/* footer */
.footer{left:0;top:3525px;width:1200px;height:304px;background:linear-gradient(180deg,#ffffff 0%,#f2f5f8 50%,#dfe7ef 100%)}
.f-brand{left:145px;top:3628px;width:290px;font-size:33px;line-height:38px;font-weight:800;color:var(--navy);text-transform:uppercase;letter-spacing:.5px}
.f-col{top:3576px}
.f-col h4{font-size:15px;font-weight:600;color:var(--navy);margin-bottom:16px}
.f-col li{list-style:none;font-size:11.5px;color:var(--text);margin-bottom:10px}
.fc1{left:494px}.fc2{left:672px}.fc3{left:843px;width:230px}
.fc3 li{display:flex;gap:10px;line-height:17px;margin-bottom:12px}
.f-rule{left:145px;top:3778px;width:911px;height:1px;background:#cfd8e1}
.copy{left:0;width:1200px;top:3798px;text-align:center;font-size:11.5px;color:var(--text)}
</style>
</head>
<body>

<div class="abs topline"></div>

<header>
  <div class="abs brand">Summit Ridge Marketing</div>
  <div class="abs contact-chip chip-mail">
    <div class="ic"><svg width="18" height="14" viewBox="0 0 18 14" fill="none" stroke="#fff" stroke-width="1.6"><rect x="1" y="1" width="16" height="12" rx="1.5"/><path d="M1 2l8 6 8-6"/></svg></div>
    <div><small>Email Us On</small><b>info@summitridge.example</b></div>
  </div>
  <div class="abs contact-chip chip-phone">
    <div class="ic"><svg width="18" height="14" viewBox="0 0 18 14" fill="none" stroke="#fff" stroke-width="1.6"><rect x="1" y="1" width="16" height="12" rx="1.5"/><path d="M1 2l8 6 8-6"/></svg></div>
    <div><small>Call Us Today</small><b>+1 555 014 2277</b></div>
  </div>
  <div class="abs navbar"></div>
  <nav class="abs nav">
    <a>Home</a><a>About Us</a><a class="active">Our Services</a><a>Clients</a><a>Testimonials</a><a>Blog</a><a>Contact Us</a>
  </nav>
</header>

<section>
  <div class="abs hero" role="img" aria-label="Snowy mountain slope with climbers hiking uphill"></div>
  <h1 class="abs hero-title">OUR SERVICES</h1>
</section>

<section>
  <h2 class="abs intro-h">Social Media <span>Marketing Services</span></h2>
  <p class="abs intro-q">Is Social Media Management Overwhelming You And Underwhelming Your Fans?</p>
  <div class="abs para intro-p">
    <p>Lorem Ipsum Dolor Sit Amet, Consectetur Adipiscing Elit, Sed Do Eiusmod Tempor Incididunt Ut Labore Et Dolore Magna Aliqua. Ut Enim Ad Minim Veniam, Quis Nostrud Exercitation Ullamco Laboris Nisi Ut Aliquip Ex Ea Commodo Consequat. Duis Aute Irure Dolor In Reprehenderit In Voluptate Velit Esse Cillum Dolore Eu Fugiat Nulla Pariatur.</p>
    <p>Sed Ut Perspiciatis Unde Omnis Iste Natus Error Sit Voluptatem Accusantium Doloremque Laudantium, Totam Rem Aperiam, Eaque Ipsa Quae Ab Illo Inventore Veritatis Et Quasi Architecto Beatae Vitae Dicta Sunt Explicabo. Nemo Enim Ipsam Voluptatem Quia Voluptas Sit Aspernatur Aut Odit Aut Fugit, Sed Quia Consequuntur Magni Dolores Eos Qui Ratione Voluptatem Sequi Nesciunt. Incidunt Ut Labore Et Dolore Magnam Aliquam Quaerat Voluptatem.</p>
  </div>
  <div class="abs photo ph1" role="img" aria-label="Hand holding a smartphone with social media reaction icons"></div>
  <div class="abs photo ph2" role="img" aria-label="Woman checking her phone on a busy evening street"></div>
  <div class="abs photo ph3" role="img" aria-label="Hands typing on a laptop with glowing digital lights"></div>
  <div class="abs photo ph4" role="img" aria-label="Team meeting around a table with sticky notes on the wall"></div>
  <div class="abs para body-p">
    <p>Lorem Ipsum Dolor Sit Amet, Consectetur Adipiscing Elit, Sed Do Eiusmod Tempor Incididunt Ut Labore Et Dolore Magna Aliqua. Ut Enim Ad Minim Veniam, Quis Nostrud Exercitation Ullamco Laboris Nisi Ut Aliquip Ex Ea Commodo Consequat. Duis Aute Irure Dolor In Reprehenderit In Voluptate Velit Esse Cillum Dolore Eu Fugiat Nulla Pariatur.</p>
    <p>At Vero Eos Et Accusamus Et Iusto Odio Dignissimos Ducimus Qui Blanditiis Praesentium Voluptatum Deleniti Atque Corrupti Quos Dolores Et Quas Molestias Excepturi Sint Occaecati Cupiditate Non Provident, Similique Sunt In Culpa Qui Officia Deserunt Mollitia Animi, Id Est Laborum Et Dolorum Fuga. Et Harum Quidem Rerum Facilis Est Et Expedita Distinctio.</p>
  </div>
</section>

<div class="abs band band1" role="img" aria-label="Snow-capped mountain range fading into mist"></div>

<section>
  <div class="abs eyebrow app-eyebrow">Our Approach</div>
  <h2 class="abs app-h">Insight. Creativity. Technology.</h2>
  <div class="abs step s1">
    <div class="badge"><svg width="40" height="40" viewBox="0 0 40 40" fill="none" stroke="#fff" stroke-width="1.8"><circle cx="20" cy="16" r="9"/><path d="M16 26h8M17 30h6M20 11v5"/></svg></div>
    <h3>Concept</h3>
    <p>Lorem Ipsum Dolor Sit Amet, Consectetur Adipiscing Elit, Sed Eiusmod Tempor Incididunt Exercitation Ullamco Laboris Nisi Ut Aliquip Ex Ut Labore Et Dolore Magna Aliqua.</p>
  </div>
  <div class="abs step s2">
    <div class="badge"><svg width="40" height="40" viewBox="0 0 40 40" fill="none" stroke="#fff" stroke-width="1.8"><path d="M7 15h26l-3-7H10z"/><rect x="9" y="15" width="22" height="17"/><rect x="16" y="22" width="8" height="10"/></svg></div>
    <h3>Build</h3>
    <p>Lorem Ipsum Dolor Sit Amet, Consectetur Adipiscing Elit, Sed Eiusmod Tempor Incididunt Exercitation Ullamco Laboris Nisi Ut Aliquip Ex Ut Labore Et Dolore Magna Aliqua.</p>
  </div>
  <div class="abs step s3">
    <div class="badge"><svg width="40" height="40" viewBox="0 0 40 40" fill="none" stroke="#fff" stroke-width="1.8"><rect x="6" y="8" width="28" height="20" rx="2"/><path d="M6 13h28M14 33h12M20 28v5M12 19h8M12 23h12"/></svg></div>
    <h3>Test</h3>
    <p>Lorem Ipsum Dolor Sit Amet, Consectetur Adipiscing Elit, Sed Eiusmod Tempor Incididunt Exercitation Ullamco Laboris Nisi Ut Aliquip Ex Ut Labore Et Dolore Magna Aliqua.</p>
  </div>
</section>

<div class="abs band band2" role="img" aria-label="Snow-capped mountain range fading into mist"></div>

<h2 class="abs ready">Are You Ready To Discover How Summit Ridge Marketing<br>Can Elevate Your Business To New Heights?</h2>

<section>
  <div class="abs c-eyebrow">Contact Us</div>
  <h2 class="abs c-h">How Can I Help You?</h2>
  <p class="abs c-sub">Fill in the form or drop an email</p>

  <div class="abs info-card card1">
    <svg width="32" height="34" viewBox="0 0 32 34" fill="none" stroke="#0b2f4e" stroke-width="1.8"><path d="M16 32s11-11 11-19A11 11 0 0 0 5 13c0 8 11 19 11 19z"/><circle cx="16" cy="13" r="4"/></svg>
    <div><b>Address</b><span>48 Alpine Lane Pinecrest&nbsp; USA 2121</span></div>
  </div>
  <div class="abs info-card card2">
    <svg width="34" height="34" viewBox="0 0 34 34" fill="none" stroke="#0b2f4e" stroke-width="1.8"><path d="M8 4l5 1 2 7-3 2c2 4 5 7 9 9l2-3 7 2 1 5c-1 2-3 3-5 3C15 30 4 19 4 9c0-2 2-4 4-5z"/><path d="M20 4a10 10 0 0 1 10 10M20 9a5 5 0 0 1 5 5"/></svg>
    <div><b>Phone Number</b><span>555-014-2277</span></div>
  </div>
  <div class="abs info-card card3">
    <svg width="36" height="32" viewBox="0 0 36 32" fill="none" stroke="#0b2f4e" stroke-width="1.8"><rect x="2" y="8" width="32" height="22" rx="1"/><path d="M2 9l16 12 16-12M8 8V2h20v6"/><circle cx="18" cy="9" r="3"/></svg>
    <div><b>Email Address</b><span>hello@summitridgemarketing.example</span></div>
  </div>

  <form class="abs enquire">
    <h2>Enquire Us</h2>
    <div class="field f1"><span>Company Name <i>*</i></span><svg width="14" height="14" viewBox="0 0 14 14" fill="none" stroke="#5d6670" stroke-width="1.2"><rect x="2" y="1" width="10" height="12"/><path d="M5 4h1M8 4h1M5 7h1M8 7h1M6 13v-3h2v3"/></svg></div>
    <div class="field f2"><span>Your Name <i>*</i></span><svg width="14" height="14" viewBox="0 0 14 14" fill="none" stroke="#5d6670" stroke-width="1.2"><circle cx="7" cy="4.5" r="3"/><path d="M1.5 13c0-3 2.5-5 5.5-5s5.5 2 5.5 5"/></svg></div>
    <div class="field f3"><span>Email <i>*</i></span><svg width="14" height="12" viewBox="0 0 14 12" fill="none" stroke="#5d6670" stroke-width="1.2"><rect x="1" y="1" width="12" height="10" rx="1"/><path d="M1 2l6 5 6-5"/></svg></div>
    <div class="field f4"><span>Phone Number <i>*</i></span><svg width="14" height="14" viewBox="0 0 14 14" fill="none" stroke="#5d6670" stroke-width="1.2"><path d="M3 1l2 .5 1 3-1.5 1c1 2 2 3 4 4l1-1.5 3 1L13 11c-.5 1-1.5 2-2.5 2C6 13 1 8 1 3.5 1 2.5 2 1.5 3 1z"/></svg></div>
    <div class="field f5"><span>Message <i>*</i></span><svg width="14" height="14" viewBox="0 0 14 14" fill="none" stroke="#5d6670" stroke-width="1.2"><rect x="1" y="2" width="12" height="11" rx="1"/><path d="M1 5h12M4 1v2M10 1v2M4 8h2M8 8h2M4 10h2"/></svg></div>
    <div class="submit">SUBMIT NOW <svg width="10" height="10" viewBox="0 0 10 10" fill="none" stroke="#fff" stroke-width="1.5"><path d="M2 8l6-6M3 2h5v5"/></svg></div>
  </form>
</section>

<section>
  <div class="abs forest" role="img" aria-label="Misty pine forest with birds flying over distant hills"></div>
  <div class="abs consult"></div>
  <div class="abs person" role="img" aria-label="Smiling woman sitting cross-legged with a laptop, giving a thumbs up"></div>
  <div class="abs consult-eyebrow">CONTACT NOW FOR A</div>
  <h2 class="abs consult-h">FREE CONSULTATION</h2>
  <div class="abs consult-btn">CONTACT US <svg width="10" height="10" viewBox="0 0 10 10" fill="none" stroke="#fff" stroke-width="1.5"><path d="M2 8l6-6M3 2h5v5"/></svg></div>
</section>

<footer>
  <div class="abs footer" role="img" aria-label="Faint snowy mountain backdrop"></div>
  <div class="abs f-brand">Summit Ridge Marketing</div>
  <div class="abs f-col fc1"><h4>Quick Links</h4><ul><li>Home</li><li>About Us</li><li>Our Services</li><li>Testimonials</li><li>Contact Us</li></ul></div>
  <div class="abs f-col fc2"><h4>Other Links</h4><ul><li>Privacy &amp; Security</li><li>Terms of Use</li><li>Cookies Policy</li><li>Site Map</li></ul></div>
  <div class="abs f-col fc3"><h4>Contact Info</h4><ul>
    <li><svg width="10" height="13" viewBox="0 0 10 13" fill="#1479bd"><path d="M5 0a5 5 0 0 1 5 5c0 3.5-5 8-5 8S0 8.5 0 5a5 5 0 0 1 5-5zm0 3a2 2 0 1 0 0 4 2 2 0 0 0 0-4z"/></svg><span>48 Alpine Lane Pinecrest<br>USA 2121</span></li>
    <li><svg width="11" height="11" viewBox="0 0 14 14" fill="#1479bd"><path d="M3 0l3 1 1 3-2 1.5c1 2 2.5 3.5 4.5 4.5L11 8l3 1 0 3c-.5 1-1.5 2-3 2C5 14 0 9 0 3 0 1.5 1.5 0 3 0z"/></svg><span>555-014-2277</span></li>
    <li><svg width="12" height="10" viewBox="0 0 12 10" fill="#1479bd"><path d="M0 1h12v8H0zM0 1l6 4 6-4" stroke="#fff" stroke-width=".8"/></svg><span>hello@summitridgemarketing.example</span></li>
  </ul></div>
  <div class="abs f-rule"></div>
  <div class="abs copy">Copyright © 2024&nbsp; Summit Ridge Marketing. All rights reserved.</div>
</footer>

</body>
</html>
```